Silver Hollow 200 Day on Grain Packaging Design

Hi there,
We are Silver Hollow Wagyu; a wagyu beef company based in Christchurch, New Zealand. We are needing new packaging for our new line of 200 day on grain ribeye / rump and sirloin steaks. Three of the same design, swapping out the text with whether is it either sirloin, ribeye or rump
About us: Silver Hollow Wagyu began in 2015 and has since been tirelessly rearing stock to the quality and levels needed to supply the best restaurants and consumers. We combine the origin of Japanese breeding genetics and 200 year old techniques with New Zealand’s grass, grain, water and air.
Website:
https://silverhollow.co.nz/
Brand Guidelines:
https://sites.pelmora.com/view/silverhollowbrandguide/home?authuser=0
The packaging dimensions are 376 x 210mm - I have attached an AI file with where the fold lines need to be, but apart from that there is free reign as long as it fits within our brand guidelines. We are open to different backgrounds with images.
The required text that needs to be on the packaging is :
Our logo
250g (approx) - this will be for Rump
200g (approx) - this will be for Sirloin and Ribeye
Wagyu Rump / Wagyu Sirloin / Wagyu Ribeye (one per design)
Proudly Farmed in New Zealand
Fresh Wagyu - Keep me chilled at or below 4°c
Frozen Wagyu - Keep me frozen below -18°c
42 Tarrow Lane, Kelvale, Christchurch, New Zealand
If you need additional imagery or further questions please don't hesitate to contact us at the following emails below.
contact@silverhollow.co.nz
info@silverhollow.co.nz
tomas.ferrante@kiwiherdline.com
Look and feel
Each slider illustrates characteristics of the customer's brand and the style your logo design should communicate.

```html
<!DOCTYPE html>
<html lang="en">
<head>
<meta charset="utf-8">
<title>Silver Hollow Wagyu – Rump Sleeve</title>
<link href="https://fonts.googleapis.com/css2?family=Montserrat:wght@300;700&display=swap" rel="stylesheet">
<style>
  :root {
    --page-bg: #ececec;
    --sleeve-black: #141516;
    --sleeve-charcoal: #222526;
    --slate-light: #4a4b4c;
    --slate-dark: #0e0f10;
    --ink-white: #f2f2f2;
    --rule-grey: #8a8c8e;
    --accent-red: #d8232f;
  }
  * { box-sizing: border-box; margin: 0; padding: 0; }
  html, body {
    width: 1200px; height: 900px; overflow: hidden;
    background: var(--page-bg);
    font-family: "Montserrat", sans-serif;
  }
  .sleeve {
    position: absolute; left: 100px; top: 170px;
    width: 1000px; height: 560px;
    background: linear-gradient(160deg, var(--sleeve-charcoal) 0%, var(--sleeve-black) 55%, #0b0c0d 100%);
    overflow: hidden;
    box-shadow: 0 20px 40px rgba(0,0,0,0.18);
  }
  .label-window {
    position: absolute; left: 120px; top: 70px;
    width: 400px; height: 140px;
    border: 1.5px solid var(--ink-white);
    border-radius: 18px;
  }
  .product-photo {
    position: absolute; left: 0; top: 250px;
    width: 720px; height: 310px;
    background:
      radial-gradient(ellipse at 48% 55%, #8d8c89 0%, #55575a 22%, rgba(40,42,44,0) 48%),
      radial-gradient(ellipse at 14% 60%, rgba(230,230,230,0.55) 0%, rgba(230,230,230,0) 12%),
      linear-gradient(120deg, var(--slate-dark) 0%, var(--slate-light) 60%, #3a3b3c 100%);
  }
  .brand-mark {
    position: absolute; left: 720px; top: 95px;
    display: flex; align-items: flex-start; gap: 14px;
  }
  .brand-dot {
    width: 12px; height: 12px; border-radius: 50%;
    background: var(--accent-red); margin-top: 14px;
  }
  .brand-name {
    color: var(--ink-white);
    font-weight: 700; font-size: 38px; line-height: 1.15;
    letter-spacing: 0.32em; text-transform: uppercase;
  }
  .brand-name .line-small { font-size: 22px; letter-spacing: 0.5em; }
  .spec-table {
    position: absolute; left: 640px; top: 290px;
    display: grid; grid-template-columns: 140px 130px; grid-template-rows: 44px 44px;
    border: 1px solid var(--rule-grey);
    color: var(--ink-white); font-weight: 300;
  }
  .spec-cut {
    grid-row: 1 / span 2; border-right: 1px solid var(--rule-grey);
    display: flex; flex-direction: column; justify-content: center;
    padding-left: 16px; font-size: 20px; line-height: 1.2; text-transform: uppercase;
  }
  .spec-grade {
    border-bottom: 1px solid var(--rule-grey);
    display: flex; align-items: center; padding-left: 16px; font-size: 20px;
  }
  .spec-weight {
    display: flex; flex-direction: column; justify-content: center;
    padding-left: 16px; font-size: 20px; line-height: 1;
  }
  .spec-weight small { font-size: 8px; letter-spacing: 0.08em; margin-top: 2px; }
  .grain-badge { position: absolute; left: 610px; top: 405px; }
</style>
</head>
<body>
  <div class="sleeve">
    <div class="label-window"></div>

    <div class="product-photo" role="img"
         aria-label="Black and white photo of a marbled wagyu rump steak on dark slate with a pinch of salt and a bay leaf"></div>

    <div class="brand-mark">
      <span class="brand-dot"></span>
      <div class="brand-name">Silver<br>Hollow<br><span class="line-small">Wagyu</span></div>
    </div>

    <div class="spec-table">
      <div class="spec-cut"><span>Wagyu</span><span>Rump</span></div>
      <div class="spec-grade">BMS 6+</div>
      <div class="spec-weight">250g<small>approx</small></div>
    </div>

    <svg class="grain-badge" width="120" height="120" viewBox="0 0 120 120" aria-hidden="true">
      <circle cx="60" cy="60" r="56" fill="none" stroke="var(--ink-white)" stroke-width="2"/>
      <circle cx="60" cy="60" r="30" fill="none" stroke="var(--ink-white)" stroke-width="1.5"/>
    </svg>
  </div>
</body>
</html>
```